Scheduled Servicing Forms

Corvella Systems requires two schedule servicing forms to be created on designer templates for our engineers to complete when servicing customers. We will complete these forms on a periodic basis, and send to the customer on completion of the work.
We have two forms that need to be created:
• Hybrid Cloud Customer Service
• Veltrix Cloud Customer Service
Please do not reference our website for ideas as its about to change. “Specialised Consulting” is our new go to market, not “Pushing the Boundaries of Technology. Our new website (still under development) is available at https://corvellasystems.qzt.net.au and will be officially launched shortly.
Our company theme is “Blue” and we want to keep a blue theme for the work.
Please ensure there is “Ample” space for engineers to write comments next to each audit item.
We have uploaded examples of the content that needs to be created for both form in Word and Excel format.
The designer must upload the source files (not just PDF) so we can edit the content on the forms at a later date.
The forms must be in standard A4 size (multiple pages).
Industry/Entity Type
Information Technology
Look and feel

```html
<!DOCTYPE html>
<html lang="en">
<head>
<meta charset="utf-8">
<title>Corvella Systems – Scheduled Service Checklist</title>
<link href="https://fonts.googleapis.com/css2?family=Source+Sans+3:wght@400;600;700&family=Montserrat:wght@600&display=swap" rel="stylesheet">
<style>
:root{
  --navy:#22256a;
  --blue:#3a86c8;
  --band:#e3e8f1;
  --ink:#222;
  --rule:#9aa3b3;
  --paper:#fff;
  --canvas:#f2f3f6;
}
*{box-sizing:border-box;margin:0;padding:0}
html,body{width:1200px;height:340px;overflow:hidden;background:var(--canvas);font-family:"Source Sans 3",sans-serif;color:var(--ink)}
.sheet{position:absolute;top:0;width:228px;height:340px;background:var(--paper);overflow:hidden}
.topband{height:20px;background:linear-gradient(var(--band),#eef1f6);position:relative}
.wordmark{position:absolute;right:8px;top:6px;display:flex;align-items:center;gap:3px;font-family:"Montserrat",sans-serif;font-weight:600;font-size:7px;color:var(--navy);letter-spacing:.3px}
.wordmark i{display:block;width:5px;height:5px;background:var(--navy)}
.checklist{position:absolute;left:8px;right:8px;top:21px;bottom:9px;display:flex;flex-direction:column;border:.5px solid #bbb}
.thead{display:flex;height:11px;flex:none;background:var(--navy);color:#fff;font-weight:700;font-size:5.6px;align-items:center}
.thead .h-item{width:60px;padding-left:3px;border-right:1px solid #fff;height:100%;display:flex;align-items:center}
.thead .h-res{flex:1;text-align:center}
.row{display:flex;flex:1;border-top:1px solid #fff;min-height:0}
.row.tall{flex:2}
.label{width:60px;flex:none;padding:2px 2px;font-size:4.2px;line-height:1.25;color:#fff;background:var(--blue);overflow:hidden}
.row.n .label{background:var(--navy)}
.res{flex:1;display:flex;flex-direction:column;justify-content:space-around;padding:1px 4px;border-bottom:.5px solid #ccd;min-width:0}
.yn{display:flex;align-items:flex-end;font-size:4.2px;height:8px;white-space:nowrap}
.box{width:5.5px;height:5.5px;border:.5px solid #555;margin-right:3px;flex:none}
.yn .opt{width:9px}
.cm{margin-left:3px;margin-right:2px}
.ln{flex:1;border-bottom:.5px solid var(--rule);margin-left:2px;margin-bottom:.5px}
.dt{width:40px;border-bottom:.5px solid var(--rule);margin-left:3px;display:flex;justify-content:space-around;margin-bottom:.5px}
.num{width:5px;margin-left:14.5px}
.link{color:#8fc3ef}
.cover-band{height:48px;background:linear-gradient(var(--band),#eef1f6);position:relative}
.cover-mark{position:absolute;left:10px;top:17px;display:flex;align-items:center;gap:4px;font-family:"Montserrat",sans-serif;font-weight:600;font-size:8.6px;color:var(--navy)}
.cover-mark i{display:block;width:12px;height:12px;background:var(--navy)}
.title-box{position:absolute;left:131px;right:7px;background:var(--navy);color:#fff;padding-left:4px;display:flex;align-items:center;border:.5px solid #fff;white-space:nowrap}
.title-box.t1{top:8px;height:16px;font-size:6.4px}
.title-box.t2{top:25px;height:16px;font-size:6.4px;font-weight:700}
.field{position:absolute;font-size:4.6px;display:flex;align-items:flex-end}
.cover .checklist{top:71px;bottom:13px}
.signoff{position:absolute;left:8px;font-size:4.4px;display:flex;align-items:flex-end}
.signoff span:first-child{width:32px}
</style>
</head>
<body>

<section class="sheet cover" style="left:0">
  <div class="cover-band">
    <div class="cover-mark"><i></i>CORVELLA SYSTEMS</div>
    <div class="title-box t1">Veltrix Hybrid/On-Premise</div>
    <div class="title-box t2">Scheduled Service Checklist</div>
  </div>
  <div class="field" style="left:9px;right:7px;top:51px">Customer:<span class="ln"></span></div>
  <div class="field" style="left:130px;right:7px;top:61px">Date:<span class="ln"></span></div>
  <div class="field" style="left:9px;width:121px;top:61px"><span class="ln" style="margin-left:0"></span></div>
  <div class="checklist">
    <div class="thead"><div class="h-item">Maintenance Check</div><div class="h-res">Result</div></div>
    <div class="row"><div class="label">Active backup for all 365 accounts (manual check) - ensuring all items are included in the job</div><div class="res"><div class="yn"><span class="box"></span><span class="opt">Yes</span><span class="cm">Comment:</span><span class="ln"></span></div><div class="yn"><span class="box"></span><span class="opt">No</span><span class="ln"></span></div></div></div>
    <div class="row n"><div class="label">Test restore from server backup</div><div class="res"><div class="yn"><span class="box"></span><span class="opt">Yes</span><span class="cm">Comment:</span><span class="ln"></span></div><div class="yn"><span class="box"></span><span class="opt">No</span><span class="ln"></span></div></div></div>
    <div class="row"><div class="label">Test restore of an email</div><div class="res"><div class="yn"><span class="box"></span><span class="opt">Yes</span><span class="cm">Comment:</span><span class="ln"></span></div><div class="yn"><span class="box"></span><span class="opt">No</span><span class="ln"></span></div></div></div>
    <div class="row n"><div class="label">Test restore of ShareDeck file</div><div class="res"><div class="yn"><span class="box"></span><span class="opt">Yes</span><span class="cm">Comment:</span><span class="ln"></span></div><div class="yn"><span class="box"></span><span class="opt">No</span><span class="ln"></span></div></div></div>
    <div class="row"><div class="label">Log into Antivirus products (ensure all endpoint devices have active antivirus and are up to date)</div><div class="res"><div class="yn"><span class="box"></span><span class="opt">Yes</span><span class="cm">Comment:</span><span class="ln"></span></div><div class="yn"><span class="box"></span><span class="opt">No</span><span class="ln"></span></div></div></div>
    <div class="row n"><div class="label">Check Spam filters</div><div class="res"><div class="yn"><span class="box"></span><span class="opt">Yes</span><span class="cm">Comment:</span><span class="ln"></span></div><div class="yn"><span class="box"></span><span class="opt">No</span><span class="ln"></span></div></div></div>
    <div class="row"><div class="label">Check that all users have MFA enabled</div><div class="res"><div class="yn"><span class="box"></span><span class="opt">Yes</span><span class="cm">Comment:</span><span class="ln"></span></div><div class="yn"><span class="box"></span><span class="opt">No</span><span class="ln"></span></div></div></div>
    <div class="row n"><div class="label">Review V365 Risk Detections</div><div class="res"><div class="yn"><span class="box"></span><span class="opt">Yes</span><span class="cm">Comment:</span><span class="ln"></span></div><div class="yn"><span class="box"></span><span class="opt">No</span><span class="ln"></span></div></div></div>
    <div class="row"><div class="label">Confirm Audit Log enabled</div><div class="res"><div class="yn"><span class="box"></span><span class="opt">Yes</span><span class="cm">Comment:</span><span class="ln"></span></div><div class="yn"><span class="box"></span><span class="opt">No</span><span class="ln"></span></div></div></div>
    <div class="row n"><div class="label">Review V365 license expiry dates</div><div class="res"><div class="yn">Expiry Date:<span class="dt"><span>/</span><span>/</span></span></div><div class="yn">Comment:<span class="ln"></span></div></div></div>
  </div>
</section>

<section class="sheet" style="left:243px">
  <div class="topband"><div class="wordmark"><i></i>CORVELLA SYSTEMS</div></div>
  <div class="checklist">
    <div class="thead"><div class="h-item">Maintenance Check</div><div class="h-res">Result</div></div>
    <div class="row"><div class="label">Review external sharing in ShareDeck/DriveVault</div><div class="res"><div class="yn"><span class="box"></span><span class="opt">Yes</span><span class="cm">Comment:</span><span class="ln"></span></div><div class="yn"><span class="box"></span><span class="opt">No</span><span class="ln"></span></div></div></div>
    <div class="row n"><div class="label">Check Compliance status</div><div class="res"><div class="yn"><span class="box"></span><span class="opt">Yes</span><span class="cm">Comment:</span><span class="ln"></span></div><div class="yn"><span class="box"></span><span class="opt">No</span><span class="ln"></span></div></div></div>
    <div class="row tall"><div class="label">Check and record Veltrix security score</div><div class="res">
      <div class="yn"><span class="box"></span><span class="opt">Yes</span><span class="cm">Score:</span><span class="ln" style="flex:0 0 26px"></span><span style="margin-left:3px">Top 5 Recommendations:</span></div>
      <div class="yn"><span class="box"></span><span class="opt">No</span><span>1</span><span class="ln"></span></div>
      <div class="yn"><span class="num">2</span><span class="ln"></span></div>
      <div class="yn"><span class="num">3</span><span class="ln"></span></div>
      <div class="yn"><span class="num">4</span><span class="ln"></span></div>
      <div class="yn"><span class="num">5</span><span class="ln"></span></div>
      <div class="yn"><span style="margin-left:14.5px">Comment:</span><span class="ln"></span></div>
    </div></div>
    <div class="row n"><div class="label">Conditional access Rules (no silly Rules, Geolocation filters in place for Sanctioned Countries)</div><div class="res"><div class="yn"><span class="box"></span><span class="opt">Yes</span><span class="cm">Comment:</span><span class="ln"></span></div><div class="yn"><span class="box"></span><span class="opt">No</span><span class="ln"></span></div></div></div>
    <div class="row"><div class="label">Review security access of all privileged accounts</div><div class="res"><div class="yn"><span class="box"></span><span class="opt">Yes</span><span class="cm">Comment:</span><span class="ln"></span></div><div class="yn"><span class="box"></span><span class="opt">No</span><span class="ln"></span></div></div></div>
    <div class="row n"><div class="label">Review Application Patching and confirm all workstations &amp; servers are up to date</div><div class="res"><div class="yn"><span class="box"></span><span class="opt">Yes</span><span class="cm">Comment:</span><span class="ln"></span></div><div class="yn"><span class="box"></span><span class="opt">No</span><span class="ln"></span></div></div></div>
    <div class="row"><div class="label">Review OS Patching and confirm all workstations &amp; servers are up to date</div><div class="res"><div class="yn"><span class="box"></span><span class="opt">Yes</span><span class="cm">Comment:</span><span class="ln"></span></div><div class="yn"><span class="box"></span><span class="opt">No</span><span class="ln"></span></div></div></div>
    <div class="row n"><div class="label">Review domain expiry dates</div><div class="res"><div class="yn">Expiry Date:<span class="dt"><span>/</span><span>/</span></span></div><div class="yn">Comment:<span class="ln"></span></div></div></div>
    <div class="row"><div class="label">Review certificate expiry dates (including internal services i.e. vHub)</div><div class="res"><div class="yn">Expiry Date:<span class="dt"><span>/</span><span>/</span></span></div><div class="yn">Comment:<span class="ln"></span></div></div></div>
    <div class="row n"><div class="label">Confirm all devices are in Application Whitelisting enforcement mode</div><div class="res"><div class="yn"><span class="box"></span><span class="opt">Yes</span><span class="cm">Comment:</span><span class="ln"></span></div><div class="yn"><span class="box"></span><span class="opt">No</span><span class="ln"></span></div></div></div>
    <div class="row"><div class="label">Ensure DMARC, DKIM and SPF records are in place and up to date</div><div class="res"><div class="yn"><span class="box"></span><span class="opt">Yes</span><span class="cm">Comment:</span><span class="ln"></span></div><div class="yn"><span class="box"></span><span class="opt">No</span><span class="ln"></span></div></div></div>
  </div>
</section>

<section class="sheet" style="left:486px">
  <div class="topband"><div class="wordmark"><i></i>CORVELLA SYSTEMS</div></div>
  <div class="checklist">
    <div class="thead"><div class="h-item">Maintenance Check</div><div class="h-res">Result</div></div>
    <div class="row"><div class="label">Confirm Retention Policies is configured and time specified</div><div class="res"><div class="yn"><span class="box"></span><span class="opt">Yes</span><span class="cm">Comment:</span><span class="ln"></span></div><div class="yn"><span class="box"></span><span class="opt">No</span><span class="ln"></span></div></div></div>
    <div class="row n"><div class="label">Review Network Firewall Firmware is up to date and no ANY &lt;&gt; ANY rules in place</div><div class="res"><div class="yn"><span class="box"></span><span class="opt">Yes</span><span class="cm">Comment:</span><span class="ln"></span></div><div class="yn"><span class="box"></span><span class="opt">No</span><span class="ln"></span></div></div></div>
    <div class="row"><div class="label">Ensure critical network equipment is connected to UPS (min 20min run time)</div><div class="res"><div class="yn"><span class="box"></span><span class="opt">Yes</span><span class="cm">Comment:</span><span class="ln"></span></div><div class="yn"><span class="box"></span><span class="opt">No</span><span class="ln"></span></div></div></div>
    <div class="row n"><div class="label">Ensure Access Layer Network device firmware is up to date (Switches &amp; Access Points)</div><div class="res"><div class="yn"><span class="box"></span><span class="opt">Yes</span><span class="cm">Comment:</span><span class="ln"></span></div><div class="yn"><span class="box"></span><span class="opt">No</span><span class="ln"></span></div></div></div>
    <div class="row tall"><div class="label">Ensure the latest backup configuration for managed network devices is current or automatically backed up monthly.<br>Saved Network location must be secured</div><div class="res" style="justify-content:flex-start;gap:4px;padding-top:3px"><div class="yn"><span class="box"></span><span class="opt">Yes</span><span class="cm">Comment:</span><span class="ln"></span></div><div class="yn"><span class="box"></span><span class="opt">No</span><span class="ln"></span></div></div></div>
    <div class="row n"><div class="label">Ensure MFP's &amp; Printers drivers up to date. No Print Nightmare</div><div class="res"><div class="yn"><span class="box"></span><span class="opt">Yes</span><span class="cm">Comment:</span><span class="ln"></span></div><div class="yn"><span class="box"></span><span class="opt">No</span><span class="ln"></span></div></div></div>
    <div class="row"><div class="label">NAC Certificates are current (PEAP/EAP-TLS</div><div class="res"><div class="yn"><span class="box"></span><span class="opt">Yes</span><span class="cm">Comment:</span><span class="ln"></span></div><div class="yn"><span class="box"></span><span class="opt">No</span><span class="ln"></span></div></div></div>
    <div class="row n"><div class="label">Check DLP alerts and configuration</div><div class="res"><div class="yn"><span class="box"></span><span class="opt">Yes</span><span class="cm">Comment:</span><span class="ln"></span></div><div class="yn"><span class="box"></span><span class="opt">No</span><span class="ln"></span></div></div></div>
    <div class="row"><div class="label">Review &amp; address SIEM and SOC alerts</div><div class="res"><div class="yn"><span class="box"></span><span class="opt">Yes</span><span class="cm">Comment:</span><span class="ln"></span></div><div class="yn"><span class="box"></span><span class="opt">No</span><span class="ln"></span></div></div></div>
    <div class="row n"><div class="label">Email alerting on Firewall changes sent to <span class="link">alerts@corv.net.au</span></div><div class="res"><div class="yn"><span class="box"></span><span class="opt">Yes</span><span class="cm">Comment:</span><span class="ln"></span></div><div class="yn"><span class="box"></span><span class="opt">No</span><span class="ln"></span></div></div></div>
    <div class="row"><div class="label">Review Vulnerability Scan reports; Remediate as required</div><div class="res"><div class="yn"><span class="box"></span><span class="opt">Yes</span><span class="cm">Comment:</span><span class="ln"></span></div><div class="yn"><span class="box"></span><span class="opt">No</span><span class="ln"></span></div></div></div>
  </div>
</section>

<section class="sheet" style="left:729px">
  <div class="topband"><div class="wordmark"><i></i>CORVELLA SYSTEMS</div></div>
  <div class="checklist">
    <div class="thead"><div class="h-item">Maintenance Check</div><div class="h-res">Result</div></div>
    <div class="row"><div class="label">Confirm all Infrastructure is in Monitoring</div><div class="res"><div class="yn"><span class="box"></span><span class="opt">Yes</span><span class="cm">Comment:</span><span class="ln"></span></div><div class="yn"><span class="box"></span><span class="opt">No</span><span class="ln"></span></div></div></div>
    <div class="row n"><div class="label">Check vendor Maintenance period of all infrastructure</div><div class="res"><div class="yn"><span class="box"></span><span class="opt">Yes</span><span class="cm">Comment:</span><span class="ln"></span></div><div class="yn"><span class="box"></span><span class="opt">No</span><span class="ln"></span></div></div></div>
    <div class="row"><div class="label">Check time sync across all/critical devices</div><div class="res"><div class="yn"><span class="box"></span><span class="opt">Yes</span><span class="cm">Comment:</span><span class="ln"></span></div><div class="yn"><span class="box"></span><span class="opt">No</span><span class="ln"></span></div></div></div>
    <div class="row n"><div class="label">Check infrastructure firmware</div><div class="res"><div class="yn"><span class="box"></span><span class="opt">Yes</span><span class="cm">Comment:</span><span class="ln"></span></div><div class="yn"><span class="box"></span><span class="opt">No</span><span class="ln"></span></div></div></div>
    <div class="row"><div class="label">Review monitoring logs/portal for active alerts</div><div class="res"><div class="yn"><span class="box"></span><span class="opt">Yes</span><span class="cm">Comment:</span><span class="ln"></span></div><div class="yn"><span class="box"></span><span class="opt">No</span><span class="ln"></span></div></div></div>
    <div class="row n"><div class="label">Review monitoring logs/portal for active alerts</div><div class="res"><div class="yn"><span class="box"></span><span class="opt">Yes</span><span class="cm">Comment:</span><span class="ln"></span></div><div class="yn"><span class="box"></span><span class="opt">No</span><span class="ln"></span></div></div></div>
    <div class="row"><div class="label">Review event logs on critical servers</div><div class="res"><div class="yn"><span class="box"></span><span class="opt">Yes</span><span class="cm">Comment:</span><span class="ln"></span></div><div class="yn"><span class="box"></span><span class="opt">No</span><span class="ln"></span></div></div></div>
    <div class="row n"><div class="label">Check Backups both local and airgap</div><div class="res"><div class="yn"><span class="box"></span><span class="opt">Yes</span><span class="cm">Comment:</span><span class="ln"></span></div><div class="yn"><span class="box"></span><span class="opt">No</span><span class="ln"></span></div></div></div>
    <div class="row"><div class="label">Check transaction logs purged by backup</div><div class="res"><div class="yn"><span class="box"></span><span class="opt">Yes</span><span class="cm">Comment:</span><span class="ln"></span></div><div class="yn"><span class="box"></span><span class="opt">No</span><span class="ln"></span></div></div></div>
    <div class="row n"><div class="label">Check IdentraID sync</div><div class="res"><div class="yn"><span class="box"></span><span class="opt">Yes</span><span class="cm">Comment:</span><span class="ln"></span></div><div class="yn"><span class="box"></span><span class="opt">No</span><span class="ln"></span></div></div></div>
    <div class="row"><div class="label">Check that application proxies are up to date</div><div class="res"><div class="yn">Expiry Date:<span class="dt"><span>/</span><span>/</span></span></div><div class="yn">Comment:<span class="ln"></span></div></div></div>
    <div class="row n"><div class="label">Service Accounts are used where possible</div><div class="res"><div class="yn"><span class="box"></span><span class="opt">Yes</span><span class="cm">Comment:</span><span class="ln"></span></div><div class="yn"><span class="box"></span><span class="opt">No</span><span class="ln"></span></div></div></div>
  </div>
</section>

<section class="sheet" style="left:972px">
  <div class="topband"><div class="wordmark"><i></i>CORVELLA SYSTEMS</div></div>
  <div class="checklist" style="bottom:56px">
    <div class="thead"><div class="h-item">Maintenance Check</div><div class="h-res">Result</div></div>
    <div class="row n tall"><div class="label">Check Domain Admin, Enterprise Admin, Record Membership and last login timestamps</div><div class="res">
      <div class="yn"><span class="box"></span><span class="opt">Yes</span><span class="cm">Score:</span><span class="ln" style="flex:0 0 26px"></span><span style="margin-left:3px">Top 5 Recommendations:</span></div>
      <div class="yn"><span class="box"></span><span class="opt">No</span><span>1</span><span class="ln"></span></div>
      <div class="yn"><span class="num">2</span><span class="ln"></span></div>
      <div class="yn"><span class="num">3</span><span class="ln"></span></div>
      <div class="yn"><span class="num">4</span><span class="ln"></span></div>
      <div class="yn"><span class="num">5</span><span class="ln"></span></div>
      <div class="yn"><span style="margin-left:14.5px">Comment:</span><span class="ln"></span></div>
    </div></div>
    <div class="row"><div class="label">Check DR replication</div><div class="res"><div class="yn"><span class="box"></span><span class="opt">Yes</span><span class="cm">Comment:</span><span class="ln"></span></div><div class="yn"><span class="box"></span><span class="opt">No</span><span class="ln"></span></div></div></div>
    <div class="row n"><div class="label">Check email alerts are configured in IPMI/HostManage etc.</div><div class="res"><div class="yn"><span class="box"></span><span class="opt">Yes</span><span class="cm">Comment:</span><span class="ln"></span></div><div class="yn"><span class="box"></span><span class="opt">No</span><span class="ln"></span></div></div></div>
    <div class="row"><div class="label">Check disk space remaining on servers and SAN block storage volumes</div><div class="res"><div class="yn"><span class="box"></span><span class="opt">Yes</span><span class="cm">Comment:</span><span class="ln"></span></div><div class="yn"><span class="box"></span><span class="opt">No</span><span class="ln"></span></div></div></div>
    <div class="row n"><div class="label">Review scheduled tasks on servers</div><div class="res"><div class="yn"><span class="box"></span><span class="opt">Yes</span><span class="cm">Comment:</span><span class="ln"></span></div><div class="yn"><span class="box"></span><span class="opt">No</span><span class="ln"></span></div></div></div>
    <div class="row"><div class="label">Check EUC applications are not installed on servers</div><div class="res"><div class="yn"><span class="box"></span><span class="opt">Yes</span><span class="cm">Comment:</span><span class="ln"></span></div><div class="yn"><span class="box"></span><span class="opt">No</span><span class="ln"></span></div></div></div>
    <div class="row n"><div class="label">Server Start-up and Shutdown Sequence configured in Hypervisors</div><div class="res"><div class="yn"><span class="box"></span><span class="opt">Yes</span><span class="cm">Comment:</span><span class="ln"></span></div><div class="yn"><span class="box"></span><span class="opt">No</span><span class="ln"></span></div></div></div>
    <div class="row"><div class="label">Review rCTL/OLM Auto-Start after power loss</div><div class="res"><div class="yn"><span class="box"></span><span class="opt">Yes</span><span class="cm">Comment:</span><span class="ln"></span></div><div class="yn"><span class="box"></span><span class="opt">No</span><span class="ln"></span></div></div></div>
    <div class="row n"><div class="label">Onsite Visit (Check rack is neat, tidy and locked)</div><div class="res"><div class="yn"><span class="box"></span><span class="opt">Yes</span><span class="cm">Comment:</span><span class="ln"></span></div><div class="yn"><span class="box"></span><span class="opt">No</span><span class="ln"></span></div></div></div>
  </div>
  <div class="signoff" style="top:301px;right:40px"><span>Completed By:</span><span class="ln"></span></div>
  <div class="signoff" style="top:313px;right:40px"><span>Signature:</span><span class="ln"></span></div>
  <div class="signoff" style="top:327px;right:40px"><span>Date:</span><span class="ln"></span></div>
</section>

</body>
</html>
```